VerdantMed Business Card & Stationary
VerdantMed Pharmacy
VerdantMed Business Card & Stationary - Pharmacy/Pharmaceuticals
Creative Brief
Professional
Clara J Vandermeer RPh
Owner/Pharmacist
3870 FM 2209 Rd, Suite 200, Katy, TX 77495
281-555-0147 Can use any 10 numbers for illustration purposes
clara@verdantmed-example.com
www.verdantmed-example.com
We are looking for something very stylish and creative yet professional that will capture attention and reinforce our branding strategy efforts. We would also like to have the ability with whatever digital files are sent to us to be easily changed by printing company to so that we could interchange staff members names and titles on the business cards. Please use modern symbols for phone, mobile, fax, web. No QR code needed. Would like to see the drafts using the logo color variations (silver or gold or blue and gray/silver) in the logo upload files. Thank you.
Designers Creativity. Editable Fields - need to be able to modify and list the pharmacy's services that will be offered: Willow Health Clinic Quick and Convenient Drive Thru Compounding: Traditional, Specialty, Pet Immunizations and Health Screening Delivery
belvuto belvuto
Project is Unveiled. Looking forward to your work towards refining the cards. Thank you.

```html
<!DOCTYPE html>
<html lang="en">
<head>
<meta charset="utf-8">
<title>VerdantMed Pharmacy Stationery</title>
<link rel="stylesheet" href="https://fonts.googleapis.com/css2?family=Cormorant+Garamond:wght@500;600&family=Lato:wght@400;700&display=swap">
<style>
:root{
  --backdrop:#e8dfcf;
  --paper:#ffffff;
  --teal:#7fa9a8;
  --teal-dark:#5f8b8a;
  --teal-faint:#e9f0f0;
  --gold-dark:#6e4f27;
  --gold-light:#c8a368;
  --ink:#4a4a4a;
  --wax:#a8141c;
  --gold-band:linear-gradient(90deg,var(--gold-dark),var(--gold-light) 50%,var(--gold-dark));
}
*{box-sizing:border-box;margin:0;padding:0}
html,body{width:1200px;height:271px;overflow:hidden}
body{font-family:"Lato",sans-serif;color:var(--ink)}
.canvas{position:relative;width:1200px;height:271px;overflow:hidden}
.backdrop{position:absolute;inset:0;background:var(--backdrop)}
.item{position:absolute;background:var(--paper);box-shadow:0 1px 3px rgba(0,0,0,.25);overflow:hidden}
.brand{font-family:"Cormorant Garamond",serif;font-weight:600;color:var(--teal-dark);display:flex;align-items:center;gap:3px;white-space:nowrap}
.brand::before{content:"";width:.8em;height:.8em;border-radius:50%;background:var(--teal)}
.gold-band{position:absolute;left:0;right:0;background:var(--gold-band);color:#fff;display:flex;align-items:center;justify-content:center;gap:8px;white-space:nowrap}
.faint-mark{position:absolute;background:var(--teal-faint);border-radius:50%}

/* business cards */
.card-front{left:20px;top:100px;width:105px;height:28px}
.card-front .brand{position:absolute;left:5px;top:4px;font-size:7.5px}
.card-front .person{position:absolute;right:5px;top:3px;text-align:right;font-size:3.2px;line-height:1.3}
.card-front .person strong{font-size:3.8px;color:var(--teal-dark)}
.card-front .gold-band{bottom:0;height:7px;font-size:2.8px;gap:6px}
.card-back{left:20px;top:143px;width:105px;height:29px;background:var(--gold-band)}
.card-back .services{position:absolute;inset:4px 5px;color:#fff;font-size:3px;line-height:1.35}
.card-back .services b{font-size:3.8px}

/* letterhead */
.letterhead{left:122px;top:26px;width:146px;height:234px}
.letterhead .brand{position:absolute;left:50%;transform:translateX(-50%);top:10px;font-size:11px}
.letterhead .faint-mark{left:33px;top:130px;width:80px;height:80px}
.letterhead .letter{position:relative;margin:38px 14px 0;font-size:3.6px;line-height:1.6}
.letterhead .letter p{margin-bottom:4px}
.letterhead .gold-band{bottom:0;height:14px;font-size:3.2px;gap:6px}

/* note card */
.note-card{left:456px;top:24px;width:60px;height:94px}
.note-card .top{position:absolute;left:0;right:0;top:0;height:22px;background:var(--teal)}
.note-card .brand{position:absolute;left:50%;transform:translateX(-50%);top:40px;font-size:6.5px}
.note-card .gold-band{bottom:0;height:6px;font-size:2.4px}

/* cd */
.cd{left:305px;top:29px;width:76px;height:76px;border-radius:50%;border:3px solid var(--gold-light)}
.cd .hole{position:absolute;left:29px;top:29px;width:12px;height:12px;border-radius:50%;border:1px solid #ccc;background:var(--backdrop)}
.cd .brand{position:absolute;left:50%;transform:translateX(-50%);top:48px;font-size:6.5px}

/* compliment slip */
.slip{left:432px;top:150px;width:72px;height:40px}
.slip .brand{position:absolute;left:50%;transform:translateX(-50%);top:10px;font-size:7px}
.slip .gold-band{bottom:0;height:6px;font-size:2.4px}

/* envelopes */
.window-envelope{left:336px;top:206px;width:168px;height:40px}
.window-envelope .brand{position:absolute;left:7px;top:5px;font-size:6.5px}
.window-envelope .window{position:absolute;left:18px;top:18px;width:52px;height:12px;border:1px solid #cfcfcf;border-radius:2px}
.window-envelope .gold-band{bottom:0;height:5px;font-size:2.4px}
.business-envelope{left:523px;top:90px;width:173px;height:58px}
.business-envelope .brand{position:absolute;left:8px;top:6px;font-size:7px}
.business-envelope .gold-band{bottom:0;height:8px;font-size:2.8px}
.wax-seal{position:absolute;left:557px;top:17px;width:42px;height:42px;border-radius:50%;background:radial-gradient(circle at 40% 35%,#d2343b,var(--wax));box-shadow:0 1px 3px rgba(0,0,0,.3)}
.flap-envelope{left:523px;top:192px;width:173px;height:54px}
.flap-envelope svg{position:absolute;inset:0}

/* large envelope */
.large-envelope{left:732px;top:12px;width:144px;height:250px}
.large-envelope svg{position:absolute;left:0;top:0}
.large-envelope .brand{position:absolute;left:50%;transform:translateX(-50%);top:74px;font-size:10px}
.large-envelope .gold-band{bottom:0;height:12px;font-size:3px}

/* folder */
.folder{left:888px;top:12px;width:290px;height:250px;background:var(--teal)}
.folder .faint-mark{left:95px;top:24px;width:100px;height:100px;background:rgba(255,255,255,.18)}
.folder .brand{position:absolute;left:50%;transform:translateX(-50%);top:124px;font-size:15px;color:#fff}
.folder .brand::before{background:#fff}
.folder svg{position:absolute;left:0;bottom:0}
</style>
</head>
<body>
<div class="canvas">
  <div class="backdrop" role="img" aria-label="Soft cream damask pattern backdrop"></div>

  <section class="item card-front">
    <div class="brand">VerdantMed</div>
    <div class="person"><strong>Clara J Vandermeer RPh</strong><br>Owner/Pharmacist<br>281-555-0147<br>clara@verdantmed-example.com</div>
    <div class="gold-band"><span>120 Sample Way, Suite 4, Townsville</span><span>www.verdantmed-example.com</span></div>
  </section>

  <section class="item card-back">
    <div class="services"><b>VerdantMed Pharmacy</b><br>Walk-In Care Corner · Quick and Convenient Drive Thru<br>Compounding: Traditional, Specialty, Pet<br>Immunizations and Health Screening · Delivery</div>
  </section>

  <section class="item letterhead">
    <div class="faint-mark" role="img" aria-label="Faint brand decoration area"></div>
    <div class="brand">VerdantMed</div>
    <div class="letter">
      <p>Date</p>
      <p>Patient Name</p>
      <p>Dear Patient,</p>
      <p>Thank you for choosing our pharmacy for your care. We look forward to serving your family with attention, trust and quality every day.</p>
      <p>Sincerely,<br><br>Clara J Vandermeer RPh<br>Owner/Pharmacist</p>
    </div>
    <div class="gold-band"><span>120 Sample Way, Suite 4, Townsville</span><span>281-555-0147</span><span>www.verdantmed-example.com</span></div>
  </section>

  <section class="item cd">
    <div class="hole"></div>
    <div class="brand">VerdantMed</div>
  </section>

  <section class="item note-card">
    <div class="top"></div>
    <div class="brand">VerdantMed</div>
    <div class="gold-band"><span>www.verdantmed-example.com</span></div>
  </section>

  <div class="wax-seal" role="img" aria-label="Red wax seal"></div>

  <section class="item slip">
    <div class="brand">VerdantMed</div>
    <div class="gold-band"><span>www.verdantmed-example.com</span></div>
  </section>

  <section class="item window-envelope">
    <div class="brand">VerdantMed</div>
    <div class="window"></div>
    <div class="gold-band"><span>120 Sample Way, Suite 4, Townsville</span></div>
  </section>

  <section class="item business-envelope">
    <div class="brand">VerdantMed</div>
    <div class="gold-band"><span>120 Sample Way, Suite 4, Townsville</span><span>www.verdantmed-example.com</span></div>
  </section>

  <section class="item flap-envelope">
    <svg width="173" height="54" viewBox="0 0 173 54"><path d="M0 0 L86.5 30 L173 0" fill="none" stroke="#d6d6d6" stroke-width="1"/><rect x="0" y="48" width="173" height="6" fill="#b08a52"/></svg>
  </section>

  <section class="item large-envelope">
    <svg width="144" height="60" viewBox="0 0 144 60"><path d="M0 0 H144 L72 56 Z" fill="var(--teal)"/></svg>
    <div class="brand">VerdantMed</div>
    <div class="gold-band"><span>www.verdantmed-example.com</span></div>
  </section>

  <section class="item folder">
    <div class="faint-mark" role="img" aria-label="Faint brand decoration area"></div>
    <div class="brand">VerdantMed</div>
    <svg width="290" height="90" viewBox="0 0 290 90"><path d="M0 30 L290 0 V90 H0 Z" fill="#ffffff"/><path d="M0 30 L290 0" stroke="#b08a52" stroke-width="2"/></svg>
  </section>
</div>
</body>
</html>
```